Card design for Heating and Cooling company

this is for a heating and cooling company we recently updated our logo and need to update our cards. We attached our logo so you can incorporate it into the card. We specialize in residential and commercial furnace and air condition repairs. Have been in business since 2014.

Phone number 555.284.9137

We need the following phrases
:Repairs, Installations, and maintenance
:Quality work at reasonable prices
:residential/commercial
:Licensed &Insured
:Email Pinegrovehvac47@mailbox-example.com
Name: Teodor K (Ted)
Also on back side I would like my logo with wording :Thank you for your business and refferal

Industry/Entity Type

Hvac

Contact Information for Business Card

:residential/commercial
:Licensed & Insured
Name: Teodor K (Ted)
Number:555.284.9136

Requirements
Must have
• Blue and red colors
Nice to have
• Maybe a pic of a furnace or air conditioner

```html
<!DOCTYPE html>
<html lang="en">
<head>
<meta charset="utf-8">
<title>Pinegrove Heating &amp; Cooling – Business Card</title>
<link rel="stylesheet" href="https://fonts.googleapis.com/css2?family=Mulish:wght@400;600;800&display=swap">
<style>
  :root {
    --stage: #262626;
    --card-dark: #1b1b1c;
    --card-light: #ffffff;
    --ink: #1a1a1a;
    --ink-soft: #2b2b2b;
    --rule: #3a3a3a;
    --blue: #2ea3e3;
    --blue-light: #7fd0f3;
    --orange: #f7a21b;
    --orange-deep: #f26a1b;
    --red: #e8261f;
    --white: #ffffff;
  }
  * { box-sizing: border-box; margin: 0; padding: 0; }
  html, body {
    width: 1200px; height: 895px; overflow: hidden;
    background: var(--stage);
    font-family: "Mulish", Arial, sans-serif;
  }
  .canvas { position: relative; width: 1200px; height: 895px; }

  .card {
    position: absolute; left: 250px; width: 700px; height: 400px;
    border-radius: 20px; overflow: hidden;
    box-shadow: 0 10px 30px rgba(0,0,0,.45);
  }
  .card--back { top: 30px; background: var(--card-dark); }
  .card--front { top: 465px; background: var(--card-light); }

  .brand {
    position: absolute; left: 0; right: 0;
    display: flex; align-items: center; justify-content: center; gap: 12px;
    font-weight: 800; letter-spacing: .02em;
  }
  .brand__dot { width: 18px; height: 18px; border-radius: 50%; background: var(--blue); }
  .card--back .brand { top: 150px; font-size: 34px; color: var(--white); }
  .card--front .brand { top: 55px; font-size: 28px; color: var(--ink); }

  .back__thanks {
    position: absolute; left: 0; right: 0; top: 290px;
    text-align: center; color: var(--white);
    font-size: 16px; font-weight: 600; letter-spacing: .06em;
  }

  .rule { position: absolute; height: 1px; background: var(--rule); }
  .rule--top { left: 330px; right: 30px; top: 132px; }
  .rule--bottom { left: 30px; width: 300px; top: 272px; }

  .contact {
    position: absolute; right: 34px; top: 144px; text-align: right;
  }
  .contact__name {
    font-family: "Mulish", Arial, sans-serif;
    color: var(--blue); font-size: 32px; font-weight: 400; letter-spacing: .01em;
    line-height: 40px; margin-bottom: 4px;
  }
  .contact__line {
    display: flex; justify-content: flex-end; align-items: center; gap: 10px;
    color: var(--ink-soft); font-size: 16px; line-height: 22px; margin-top: 4px;
  }
  .contact__line svg { width: 16px; height: 16px; flex: none; }

  .services {
    position: absolute; left: 36px; top: 284px; list-style: none;
    color: var(--ink); font-size: 18px; line-height: 24px;
  }
  .services li { display: flex; align-items: center; gap: 12px; }
  .services li::before {
    content: ""; width: 8px; height: 8px; border-radius: 50%;
    background: var(--bullet);
  }
  .services li:nth-child(1) { --bullet: var(--red); }
  .services li:nth-child(2) { --bullet: var(--orange-deep); }
  .services li:nth-child(3) { --bullet: #f4861c; }
  .services li:nth-child(4) { --bullet: var(--orange); }

  .edge-band {
    position: absolute; left: 0; right: 0; bottom: 0; height: 8px;
    background: linear-gradient(90deg, var(--blue) 0%, var(--blue-light) 56%, var(--orange) 57%, var(--orange-deep) 78%, var(--red) 100%);
  }
</style>
</head>
<body>
<main class="canvas">

  <section class="card card--back" aria-label="Card back">
    <div class="brand"><span class="brand__dot"></span>Pinegrove Heating &amp; Cooling</div>
    <p class="back__thanks">Thank you for your business and refferal</p>
  </section>

  <section class="card card--front" aria-label="Card front">
    <div class="brand"><span class="brand__dot"></span>Pinegrove Heating &amp; Cooling</div>

    <div class="rule rule--top"></div>

    <div class="contact">
      <p class="contact__name">TEODOR K (TED)</p>
      <p class="contact__line">555.284.9136
        <svg viewBox="0 0 16 16" aria-hidden="true"><rect x="4" y="1" width="8" height="14" rx="1.5" fill="none" stroke="var(--blue)" stroke-width="1.5"/><circle cx="8" cy="12.5" r=".9" fill="var(--blue)"/></svg>
      </p>
      <p class="contact__line">Pinegrovehvac47@mailbox-example.com
        <svg viewBox="0 0 16 16" aria-hidden="true"><rect x="1" y="3" width="14" height="10" rx="1" fill="var(--blue)"/><path d="M1.5 3.5 8 9l6.5-5.5" fill="none" stroke="var(--white)" stroke-width="1.2"/></svg>
      </p>
    </div>

    <div class="rule rule--bottom"></div>

    <ul class="services">
      <li>Repairs, Installations, and maintenance</li>
      <li>Quality work at reasonable prices</li>
      <li>Residential/commercial</li>
      <li>Licensed &amp; Insured</li>
    </ul>

    <div class="edge-band"></div>
  </section>

</main>
</body>
</html>
```